Honey Jar Label Design

I am looking for a fun label design for a 1 lb honey jar.
The company is Corliss Waverly Botanicals, which sells cut flowers and is expanding into honey and eventually other honey products. I've included the design work for the business, and I'd like the honey products to coordinate with them but not necessarily match directly.
Label requirements:
Raw Honey
Corliss Waverly Botanicals
27308 Quarry Bend Rd
Wrenvale, NE 66341
NET WT. 16 OZ. (weight info must be in the lower third of the front label and easy to read)
Look and feel
Each slider illustrates characteristics of the customer's brand and the style your logo design should communicate.

```html
<!DOCTYPE html>
<html lang="en">
<head>
<meta charset="utf-8">
<title>Raw Honey Label – Corliss Waverly Botanicals</title>
<link rel="stylesheet" href="https://fonts.googleapis.com/css2?family=Montserrat:wght@500;700&family=Playfair+Display:wght@400;500;600&display=swap">
<style>
  :root {
    --page-bg: #ffffff;
    --label-teal: #0f2a30;
    --blush: #e1cfd0;
    --ink: #0f2a30;
  }
  * { margin: 0; padding: 0; box-sizing: border-box; }
  html, body { width: 1200px; height: 800px; overflow: hidden; background: var(--page-bg); }
  .canvas { position: relative; width: 1200px; height: 800px; background: var(--page-bg); }

  .label { position: absolute; left: 456px; top: 240px; width: 254px; height: 412px; }
  .label svg { position: absolute; inset: 0; width: 100%; height: 100%; }
  .label-border { fill: var(--label-teal); }
  .label-panel { fill: var(--blush); }

  .label-text { position: absolute; inset: 0; text-align: center; color: var(--ink); }
  .product-name {
    position: absolute; left: 0; right: 0; top: 102px;
    font-family: "Playfair Display", serif; font-weight: 600;
    font-size: 53px; line-height: 42px; letter-spacing: 0;
  }
  .brand-name {
    position: absolute; left: 0; right: 0; top: 194px;
    font-family: "Montserrat", sans-serif; font-weight: 700; font-size: 13px;
  }
  .address {
    position: absolute; left: 0; right: 0; top: 240px;
    font-family: "Montserrat", sans-serif; font-weight: 500; font-size: 13px; line-height: 17px;
  }
  .weight-rule {
    position: absolute; left: 38px; right: 38px; top: 321px;
    height: 1px; background: var(--ink);
  }
  .net-weight {
    position: absolute; left: 0; right: 0; top: 329px;
    font-family: "Montserrat", sans-serif; font-weight: 700; font-size: 20px;
  }

  .brand-seal {
    position: absolute; left: 738px; top: 123px; width: 170px; height: 170px;
    border-radius: 50%; background: var(--label-teal);
    display: flex; align-items: center; justify-content: center; text-align: center;
    padding: 30px;
  }
  .brand-seal-name {
    font-family: "Montserrat", sans-serif; font-weight: 700; font-size: 14px;
    line-height: 19px; color: var(--blush);
  }
</style>
</head>
<body>
<main class="canvas">
  <section class="label">
    <svg viewBox="0 0 254 412">
      <path class="label-border" role="img" aria-label="Dark teal label border with fine line-drawn wildflower pattern"
        d="M82 0 H172 C200 0 226 40 240 100 C250 150 254 190 254 225 C254 290 246 340 236 380 C230 402 222 412 206 412 H48 C32 412 24 402 18 380 C8 340 0 290 0 225 C0 190 4 150 14 100 C28 40 54 0 82 0 Z"/>
      <path class="label-panel"
        d="M96 37 H158 C178 37 196 60 210 100 C226 145 234 190 234 230 C234 285 228 330 220 360 C216 374 210 382 196 382 H58 C44 382 38 374 34 360 C26 330 20 285 20 230 C20 190 28 145 44 100 C58 60 76 37 96 37 Z"/>
    </svg>
    <div class="label-text">
      <h1 class="product-name">RAW<br>HONEY</h1>
      <p class="brand-name">Corliss Waverly Botanicals</p>
      <p class="address">27308 Quarry Bend Rd,<br>Wrenvale, NE 66341</p>
      <div class="weight-rule"></div>
      <p class="net-weight">NET WT. 16 OZ.</p>
    </div>
  </section>

  <aside class="brand-seal">
    <p class="brand-seal-name">Corliss Waverly Botanicals</p>
  </aside>
</main>
</body>
</html>
```